Banners needed for a rail company to showcase services and locations

We need a set of either 2 or 3 banners that have services on one and locations on the other two or one. Colors are red, grey and black. Needs to include the photos that are already on it, including a map of locations. (preferably a more modern map). It also needs to include all locations. Consistency is key as they will be next to each other and need to flow nicely together. We have attached the current proofs of the banners along with high resolution logos.
Updates

Hello, thank you for submitting your designs. I do need to add that the list of locations needs to be in the middle. Thank you!

Industry/Entity Type

Railroad

Colors

Requirements
Must have
• all wording in document # DOC030722-03072022162104 must be included
Nice to have
• modern map of locations, color (that fits the color scheme: red, grey, black, etc.)
Should not have
• no bright colors, please stick to the preference above

```html
<!DOCTYPE html>
<html lang="en">
<head>
<meta charset="utf-8">
<title>Trackline Yards – Banner Set</title>
<link href="https://fonts.googleapis.com/css2?family=Bebas+Neue&family=Montserrat:wght@300;400;600;700&display=swap" rel="stylesheet">
<style>
  :root {
    --red: #d71e25;
    --red-dark: #a8141a;
    --black: #111111;
    --charcoal: #2b2b2b;
    --grey: #8a8a8a;
    --grey-light: #d9d9d9;
    --paper: #ffffff;
    --stage: #eeeeee;
  }
  * { box-sizing: border-box; margin: 0; padding: 0; }
  html, body { width: 800px; height: 1200px; overflow: hidden; background: var(--stage); }
  body { font-family: "Montserrat", sans-serif; color: var(--charcoal); }

  .banner-set {
    position: absolute; top: 382px; left: 12px;
    display: flex; gap: 20px;
  }
  .banner {
    position: relative; width: 245px; height: 436px;
    background: var(--paper); overflow: hidden;
    box-shadow: 0 6px 14px rgba(0,0,0,.22);
  }
  .banner-shapes { position: absolute; inset: 0; }

  .brand-name {
    position: absolute; display: flex; align-items: center; gap: 4px;
    font-family: "Montserrat", sans-serif; font-weight: 700;
    font-size: 10px; letter-spacing: .5px; color: var(--charcoal); text-transform: uppercase;
    white-space: nowrap;
  }
  .brand-name .dot { width: 8px; height: 8px; border-radius: 50%; background: var(--red); }

  .footer-pill {
    position: absolute; left: 40px; top: 404px; width: 165px; height: 18px;
    background: var(--black); border-radius: 9px;
    display: flex; align-items: center; gap: 7px; padding-left: 2px;
  }
  .footer-pill .globe { flex: none; width: 14px; height: 14px; }
  .footer-pill .url {
    color: #fff; font-size: 8px; letter-spacing: .8px; font-weight: 400;
    white-space: nowrap; line-height: 1;
  }

  /* services banner */
  .headline { position: absolute; left: 0; width: 100%; top: 220px; text-align: center; color: #fff; }
  .headline .lead { font-weight: 300; font-size: 16px; line-height: 1; letter-spacing: .3px; }
  .headline .main { font-family: "Bebas Neue", sans-serif; font-size: 27px; line-height: 1; margin-top: 1px; }
  .section-tab {
    position: absolute; left: 78px; top: 283px; width: 90px; height: 27px;
    background: var(--grey); border-radius: 0 0 6px 6px;
    font-family: "Bebas Neue", sans-serif; font-size: 14px; color: var(--black);
    display: flex; align-items: center; justify-content: center;
  }
  .service-list {
    position: absolute; left: 20px; top: 333px; width: 215px;
    display: grid; grid-template-columns: 112px 103px; row-gap: 6px;
    list-style: none; font-size: 8px; line-height: 1.25;
  }
  .service-list li { display: flex; align-items: flex-start; gap: 5px; }
  .service-list .icon { flex: none; width: 11px; height: 11px; border-radius: 50%; background: var(--red); position: relative; top: -1px; }

  /* locations banner */
  .locations-tab {
    position: absolute; left: 48px; top: 180px; width: 149px; height: 40px;
    background: var(--red); border-radius: 0 0 8px 8px;
    font-family: "Bebas Neue", sans-serif; font-size: 26px; color: #fff;
    display: flex; align-items: center; justify-content: center;
  }
  .intro {
    position: absolute; left: 22px; top: 228px; width: 201px;
    font-size: 7px; line-height: 1.35; text-align: justify;
  }
  .map-card {
    position: absolute; left: 21px; top: 277px; width: 203px; height: 110px;
    border-radius: 7px; overflow: hidden; background: var(--red);
  }
  .map-area { height: 83px; background: linear-gradient(180deg, #ecebe6 0%, #e6e2d8 60%, #bcd3e6 100%); }
  .map-labels {
    display: grid; grid-template-columns: repeat(5, 1fr); height: 27px;
    align-items: center; text-align: center;
    font-size: 4.6px; font-weight: 600; color: #fff; line-height: 1.1; text-transform: uppercase;
  }
  .logo-ring {
    position: absolute; left: 72px; top: -28px; width: 101px; height: 101px;
    border-radius: 50%; background: rgba(255,255,255,.82); border: 2px solid #fff;
  }

  /* location list banner */
  .site {
    position: absolute; left: 23px; width: 199px;
    border: 1px dashed var(--grey); border-radius: 8px; text-align: center;
  }
  .site-name {
    position: absolute; left: 50%; top: -7px; transform: translateX(-50%);
    background: var(--paper); padding: 0 5px; white-space: nowrap;
    font-weight: 700; font-size: 8.5px; line-height: 12px; color: var(--charcoal); text-transform: uppercase;
    display: flex; align-items: center; gap: 3px;
  }
  .site-name .dot { width: 7px; height: 7px; background: var(--red); }
  .site-detail {
    position: absolute; left: 0; right: 0; bottom: 8px;
    font-size: 6.3px; font-weight: 600; color: var(--black); white-space: nowrap;
  }
</style>
</head>
<body>
<main class="banner-set">

  <!-- Services banner -->
  <section class="banner banner-services">
    <svg class="banner-shapes" viewBox="0 0 245 436" aria-hidden="true">
      <path d="M0 170 Q120 185 245 160 L245 292 Q130 284 0 318 Z" fill="var(--red)"/>
      <path d="M0 300 Q120 270 245 290 L245 296 Q130 290 0 326 Z" fill="var(--black)"/>
      <path d="M0 420 Q122 400 245 420 L245 436 L0 436 Z" fill="var(--grey-light)"/>
      <line x1="70" y1="266" x2="175" y2="266" stroke="#fff" stroke-width="1"/>
    </svg>
    <div role="img" aria-label="Photo of a red and black striped locomotive in a rail yard"
         style="position:absolute;left:0;top:0;width:245px;height:178px;background:linear-gradient(160deg,#c9d5e4 0%,#8e97a5 45%,#3a3d44 100%);clip-path:polygon(0 0,100% 0,100% 90%,0 96%);"></div>
    <div class="brand-name" style="left:150px;top:20px;"><span class="dot"></span>Trackline</div>
    <div class="headline">
      <p class="lead">A PRIVATELY-OWNED</p>
      <p class="main">RAIL YARD OPERATOR</p>
    </div>
    <div class="section-tab">SERVICES</div>
    <ul class="service-list">
      <li><span class="icon"></span>Railcar Storage</li>
      <li><span class="icon"></span>Transloading</li>
      <li><span class="icon"></span>Switching</li>
      <li><span class="icon"></span>Chemical Packaging</li>
      <li><span class="icon"></span>Railcar Cleaning &amp; Maintenance</li>
      <li><span class="icon"></span>Plastics Packaging</li>
    </ul>
    <div class="footer-pill">
      <svg class="globe" viewBox="0 0 14 14" aria-hidden="true"><circle cx="7" cy="7" r="7" fill="var(--red)"/><circle cx="7" cy="7" r="4" fill="none" stroke="#fff" stroke-width=".8"/><path d="M3 7h8M7 3v8" stroke="#fff" stroke-width=".8"/></svg>
      <span class="url">www.trackline-yards.com</span>
    </div>
  </section>

  <!-- Locations banner -->
  <section class="banner banner-locations">
    <div role="img" aria-label="Aerial photo of a rail park with tracks, grain silos and a truck on an overpass"
         style="position:absolute;left:0;top:0;width:245px;height:186px;background:linear-gradient(170deg,#7fa1c9 0%,#c2b79a 40%,#8d8c86 75%,#5c5f62 100%);clip-path:ellipse(140% 100% at 50% 0);"></div>
    <svg class="banner-shapes" viewBox="0 0 245 436" aria-hidden="true">
      <path d="M0 150 Q90 196 245 155 L245 162 Q100 200 0 160 Z" fill="var(--black)"/>
      <path d="M0 420 Q122 400 245 420 L245 436 L0 436 Z" fill="var(--grey-light)"/>
    </svg>
    <div class="logo-ring"></div>
    <div class="brand-name" style="left:92px;top:26px;"><span class="dot"></span>Trackline</div>
    <div class="locations-tab">LOCATIONS</div>
    <p class="intro">Trackline Yards is a privately-owned rail yard operator specializing in the storage, handling and switching of railcars for users in the petrochemical, energy, agricultural and logistics industries. Established in 2006</p>
    <div class="map-card">
      <div class="map-area" role="img" aria-label="Map of the Gulf Coast showing the five yard locations"></div>
      <div class="map-labels">
        <span>Trackline<br>Mesa<br>Junction</span>
        <span>Trackline<br>Harborline</span>
        <span>Trackline<br>Dayton</span>
        <span>Trackline<br>Bayou Bend</span>
        <span>Trackline<br>La Porte</span>
      </div>
    </div>
    <div class="footer-pill">
      <svg class="globe" viewBox="0 0 14 14" aria-hidden="true"><circle cx="7" cy="7" r="7" fill="var(--red)"/><circle cx="7" cy="7" r="4" fill="none" stroke="#fff" stroke-width=".8"/><path d="M3 7h8M7 3v8" stroke="#fff" stroke-width=".8"/></svg>
      <span class="url">www.trackline-yards.com</span>
    </div>
  </section>

  <!-- Location list banner -->
  <section class="banner banner-sites">
    <svg class="banner-shapes" viewBox="0 0 245 436" aria-hidden="true">
      <defs>
        <linearGradient id="topGrad" x1="0" y1="0" x2="0" y2="1">
          <stop offset="0" stop-color="#050505"/><stop offset="1" stop-color="#262626"/>
        </linearGradient>
      </defs>
      <path d="M0 0 H245 V78 Q110 52 0 112 Z" fill="url(#topGrad)"/>
      <path d="M0 112 Q110 52 245 78 V84 Q110 60 0 112 Z" fill="var(--red)"/>
      <path d="M0 112 Q40 68 135 58 Q60 66 0 100 Z" fill="var(--red)"/>
      <path d="M0 420 Q122 400 245 420 L245 436 L0 436 Z" fill="var(--grey-light)"/>
    </svg>
    <div class="brand-name" style="left:84px;top:30px;color:#fff;font-size:13px;"><span class="dot"></span>Trackline</div>
    <div class="site" style="top:110px;height:44px;"><span class="site-name"><span class="dot"></span>Mesa Junction Rail Park</span><p class="site-detail">SAN ANTONIO, TX = 520 ACRES / 1,200 CAR CAPACITY</p></div>
    <div class="site" style="top:174px;height:44px;"><span class="site-name"><span class="dot"></span>Harborline Industrial Park</span><p class="site-detail">BAYTOWN, TX = 200 ACRES / 3,310 CAR CAPACITY</p></div>
    <div class="site" style="top:236px;height:32px;"><span class="site-name"><span class="dot"></span>Crossway Industrial Park</span><p class="site-detail">DAYTON, TX = 300 ACRES / 1,030 CAR CAPACITY</p></div>
    <div class="site" style="top:290px;height:42px;"><span class="site-name"><span class="dot"></span>Bayou Bend Rail Terminal</span><p class="site-detail">LACASSINE, LA = 400 ACRES / 1,650 CAR CAPACITY</p></div>
    <div class="site" style="top:352px;height:38px;"><span class="site-name"><span class="dot"></span>Gulfway Commerce Center</span><p class="site-detail">LACASSINE, LA = 400 ACRES / 1,650 CAR CAPACITY</p></div>
    <div class="footer-pill">
      <svg class="globe" viewBox="0 0 14 14" aria-hidden="true"><circle cx="7" cy="7" r="7" fill="var(--red)"/><circle cx="7" cy="7" r="4" fill="none" stroke="#fff" stroke-width=".8"/><path d="M3 7h8M7 3v8" stroke="#fff" stroke-width=".8"/></svg>
      <span class="url">www.trackline-yards.com</span>
    </div>
  </section>

</main>
</body>
</html>
```